Business Card Design Project for - The Hollowmere Planting Company Ltd. We are a Landscape and garden

I would like designer to use all special glosses etc so i can have a professional looking business card. The theme of the business card can reflect that of the Logo attached by MarkQuarry or your own unique ideas.. please feel free to go wild as i hope i can select a winner i like - my budget will be committed so please get involved. Good luck and thank you Rowan

Target Market(s)

Must look Professional

General Public and Businesses including Councils, Local Government, Hospitals, Hotels, Professionals and Professional Sports People.

Industry/Entity Type

Landscape Gardening

Contact Information for Business Card

The Hollowmere Planting Company Ltd

Mr R.T Pelling
Head Office - Quayside Works Manchester
t. 0784 529 618
e. info@hollowmereplanting.co.uk
w. www.hollowmereplanting.co.uk

Facebook - https://www.friendpage.example/TheHollowmerePlantingCompany/
Twitter - https://chirpline.example/TheMossyTrowel
Instagram - https://www.snapgrid.example/thehollowmereplantingcompany/?hl=en
Google+ - https://circles.searchhub.example/u/0/208475639102847561932
Yelp - https://www.reviewden.example/biz/the-hollowmere-planting-company-manchester-4

Font styles to use
Serif
Script
Other font styles liked:
• I don't have much of an idea of font types sorry

Colors

Designer to choose colors to be used in the design.

Requirements
Must have
• A Professional look and Design
• Special effects with gloss and fading of colours possibly..
• Front and back design
Nice to have
• All special features with effects and gloss etc

```html
<!DOCTYPE html>
<html lang="en">
<head>
<meta charset="utf-8">
<title>The Hollowmere Planting Company Ltd — Business Card</title>
<link rel="stylesheet" href="https://fonts.googleapis.com/css2?family=Cinzel:wght@400;600&family=Dancing+Script:wght@600&family=Open+Sans:wght@400;600&display=swap">
<style>
  :root {
    --backdrop: #efe6da;
    --card-white: #ffffff;
    --soil: #5b3412;
    --soil-deep: #230600;
    --soil-mid: #4a2209;
    --tan: #c9a27a;
    --leaf: #39b54a;
    --leaf-light: #8dc63f;
    --ink: #4a4a4a;
    --wordmark-grey: #6d6d6d;
    --accent: #b0561c;
    --name-brown: #6b3a12;
  }
  * { box-sizing: border-box; margin: 0; padding: 0; }
  html, body { width: 1200px; height: 1200px; overflow: hidden; }
  body {
    background: var(--backdrop);
    font-family: "Open Sans", Arial, sans-serif;
    position: relative;
  }
  .card {
    position: absolute;
    left: 180px;
    width: 840px;
    height: 480px;
    overflow: hidden;
    box-shadow: 0 10px 30px rgba(60, 40, 20, 0.18);
  }
  .card--front { top: 90px; background: var(--card-white); }
  .card--back {
    top: 630px;
    background: linear-gradient(160deg, var(--soil-mid) 0%, var(--soil-deep) 100%);
  }

  /* Wordmark */
  .wordmark { position: absolute; display: flex; align-items: center; gap: 18px; }
  .wordmark__dot { width: 54px; height: 54px; border-radius: 50%; background: var(--leaf); flex: none; }
  .wordmark__text {
    font-family: "Cinzel", Georgia, serif;
    font-weight: 600;
    color: var(--wordmark-grey);
    line-height: 1.15;
  }
  .wordmark__name { display: block; font-size: 36px; letter-spacing: 2px; }
  .wordmark__tag { display: block; font-size: 15px; letter-spacing: 3px; }
  .card--front .wordmark { left: 90px; top: 90px; }
  .card--back .wordmark { left: 330px; top: 330px; }
  .card--back .wordmark__text { color: #d9d9d9; }

  /* Contact block */
  .contact {
    position: absolute;
    right: 50px;
    top: 165px;
    text-align: right;
    color: var(--ink);
    font-size: 17px;
    line-height: 1.45;
  }
  .contact__name {
    font-family: "Dancing Script", cursive;
    font-size: 40px;
    color: var(--name-brown);
    line-height: 1.1;
    margin-bottom: 2px;
  }
  .contact__label { color: var(--accent); }

  /* Social band */
  .social-band {
    position: absolute;
    left: 0; right: 0; bottom: 0;
    height: 125px;
    background: var(--soil);
    border-top: 6px solid var(--tan);
    color: #ffffff;
    font-size: 13.5px;
    padding: 30px 40px 0;
    line-height: 2;
  }
  .social-band__row { white-space: nowrap; }
  .social-band__icon {
    display: inline-block;
    width: 11px; height: 11px;
    background: #ffffff;
    margin-right: 6px;
    vertical-align: -1px;
  }
  .social-band__sep { margin: 0 8px; opacity: 0.8; }

  .leaf-field { position: absolute; left: 0; top: 0; }
</style>
</head>
<body>

<section class="card card--front" aria-label="Card front">
  <div class="wordmark">
    <span class="wordmark__dot"></span>
    <span class="wordmark__text">
      <span class="wordmark__name">The Hollowmere</span>
      <span class="wordmark__tag">Planting Company Ltd</span>
    </span>
  </div>

  <div class="contact">
    <p class="contact__name">Mr R.T Pelling</p>
    <p>Head Office</p>
    <p>Quayside Works Manchester</p>
    <p><span class="contact__label">Tel :</span> 0784 529 618</p>
    <p><span class="contact__label">Web:</span> www.hollowmereplanting.co.uk</p>
    <p><span class="contact__label">Email :</span> info@hollowmereplanting.co.uk</p>
  </div>

  <div class="social-band">
    <p class="social-band__row">
      <span class="social-band__icon"></span>TheHollowmerePlantingCompany<span class="social-band__sep">|</span>
      <span class="social-band__icon"></span>TheMossyTrowel<span class="social-band__sep">|</span>
      <span class="social-band__icon"></span>thehollowmereplantingcompany/?hl=en
    </p>
    <p class="social-band__row">
      <span class="social-band__icon"></span>208475639102847561932<span class="social-band__sep">|</span>
      <span class="social-band__icon"></span>the-hollowmere-planting-company-manchester-4
    </p>
  </div>
</section>

<section class="card card--back" aria-label="Card back">
  <svg class="leaf-field" width="520" height="400" viewBox="0 0 520 400" role="img" aria-label="Large glossy green leaf illustration">
    <defs>
      <linearGradient id="leafGlow" x1="0" y1="1" x2="1" y2="0">
        <stop offset="0" stop-color="var(--leaf-light)"/>
        <stop offset="1" stop-color="var(--leaf)"/>
      </linearGradient>
    </defs>
    <path d="M0 0 H500 C460 230 270 370 0 390 Z" fill="url(#leafGlow)"/>
  </svg>

  <div class="wordmark">
    <span class="wordmark__dot"></span>
    <span class="wordmark__text">
      <span class="wordmark__name">The Hollowmere</span>
      <span class="wordmark__tag">Planting Company Ltd</span>
    </span>
  </div>
</section>

</body>
</html>
```